Promotion for Local Garage - Corrin Motorworks offering 10% off

We are after an A5 Colour Leaflet to promote our business Corrin Motorworks.

Corrin Motorworks is a local garage and we are about to launch a flyer campaign in the local area.

Services we provide:
Servicing, Repairs, Diagnostics, Clutches, Brakes, Exhaust for all makes and models of cars and vans.

10% discount for anyone who brings in this flyer with them.

Company contact details below:
Telephone 0151 3846172
Website www.corrinmotorworks-example.co.uk

Address
Unit 4 Hollin Workshops,
Brackwell Lane,
Fenwick Ind Estate,
Ellesmere Port,
CH64 9QP

Our Logo is attached

Target Market(s)

Local Residents and businesses

Industry/Entity Type

Auto Repair

Requirements
Must have
• Services we provide:
• Servicing, Repairs, Diagnostics, Clutches, Brakes, Exhaust for all makes and models of cars and vans.
• 10% discount for anyone who brings in this flyer with them.
• Company contact details below:
• Telephone 0151 3846172
• Website www.corrinmotorworks-example.co.uk
• Address
• Unit 4 Hollin Workshops,
• Brackwell Lane,
• Fenwick Ind Estate,
• Ellesmere Port,
• CH64 9QP

```html
<!DOCTYPE html>
<html lang="en">
<head>
<meta charset="utf-8">
<title>Corrin Motorworks – A5 Leaflet</title>
<link rel="stylesheet" href="https://fonts.googleapis.com/css2?family=Bebas+Neue&family=Comic+Neue:wght@400;700&family=Dancing+Script:wght@400&display=swap">
<style>
  :root {
    --page-bg: #ffffff;
    --paper: #ffffff;
    --brand-red: #e3262b;
    --ink-dark: #1b1b1b;
    --slate: #58585a;
    --label-grey: #444444;
    --text-light: #ffffff;
  }
  * { margin: 0; padding: 0; box-sizing: border-box; }
  html, body {
    width: 1200px; height: 1000px; overflow: hidden;
    background: var(--page-bg);
  }
  .leaflet {
    position: absolute; left: 309px; top: 86px;
    width: 585px; height: 827px;
    background: var(--paper);
    box-shadow: 0 1px 4px rgba(0,0,0,0.25);
    overflow: hidden;
  }
  .masthead { position: absolute; left: 0; top: 0; width: 100%; height: 157px; }
  .address {
    position: absolute; left: 43px; top: 31px;
    font-family: "Comic Neue", cursive;
    font-style: normal; font-weight: 700;
    font-size: 13.5px; line-height: 16.5px; letter-spacing: 0.3px;
    color: var(--brand-red);
  }
  .address-label { color: var(--label-grey); font-weight: 400; letter-spacing: 0.6px; }
  .brand-name {
    position: absolute; left: 256px; top: 90px;
    font-family: "Comic Neue", cursive;
    font-weight: 700; font-size: 33px; line-height: 1;
    color: var(--slate); white-space: nowrap;
  }
  .offer-panel {
    position: absolute; left: 0; top: 157px; width: 100%; height: 495px;
    background: var(--brand-red);
  }
  .offer-line {
    position: absolute; left: 40px; top: 36px;
    color: var(--text-light); white-space: nowrap;
  }
  .offer-amount { font-family: "Bebas Neue", sans-serif; font-size: 29px; letter-spacing: 0.3px; }
  .offer-terms { font-family: "Dancing Script", cursive; font-size: 18px; letter-spacing: 1.2px; margin-left: 3px; }
  .vehicle-art {
    position: absolute; left: 36px; top: 92px; width: 510px; height: 222px;
    background: radial-gradient(ellipse at 55% 55%, #1b1b1b 0%, #2a1a1a 55%, #c42328 100%);
    border-radius: 60px 80px 20px 30px / 70px 60px 20px 30px;
  }
  .services-title {
    position: absolute; left: 37px; top: 350px;
    font-family: "Bebas Neue", sans-serif; font-size: 62px; line-height: 1;
    font-weight: 400;
    color: var(--text-light); letter-spacing: 3.6px; white-space: nowrap;
  }
  .services-list {
    position: absolute; left: 37px; top: 414px;
    font-family: "Bebas Neue", sans-serif; font-size: 20.5px; line-height: 23px;
    color: var(--text-light); letter-spacing: 1.7px; white-space: nowrap;
  }
  .contact-band {
    position: absolute; left: 0; top: 652px; width: 100%; height: 175px;
    background: var(--slate);
  }
  .contact {
    position: absolute; left: 274px; top: 60px;
    font-family: "Comic Neue", cursive; font-weight: 700;
    color: var(--text-light); text-transform: uppercase; white-space: nowrap;
  }
  .contact-phone { font-size: 24px; letter-spacing: 3.4px; line-height: 28px; }
  .contact-web { font-size: 13px; letter-spacing: 0.2px; line-height: 22px; }
</style>
</head>
<body>
  <main class="leaflet">
    <header class="masthead">
      <address class="address">
        <span class="address-label">ADDRESS</span><br>
        Unit 4 Hollin Workshops,<br>
        Brackwell Lane,<br>
        Fenwick Ind Estate,<br>
        Ellesmere Port,<br>
        CH64 9QP
      </address>
      <div class="brand-name">Corrin Motorworks</div>
    </header>

    <section class="offer-panel">
      <p class="offer-line"><span class="offer-amount">10% Discount</span><span class="offer-terms">for anyone who brings in this flyer with them</span></p>
      <div class="vehicle-art" role="img" aria-label="Black silhouette illustration of a sports car, three-quarter front view"></div>
      <h1 class="services-title">SERVICES WE PROVIDE:</h1>
      <p class="services-list">SERVICING, REPAIRS, DIAGNOSTICS, CLUTCHES, BRAKES, EXHAUST<br>FOR ALL MAKES AND MODELS OF CARS AND COMMERCIAL VEHICLES</p>
    </section>

    <footer class="contact-band">
      <div class="contact">
        <p class="contact-phone">Tel: 0151 3846172</p>
        <p class="contact-web">www.corrinmotorworks-example.co.uk</p>
      </div>
    </footer>
  </main>
</body>
</html>
```